Fachgeschäft für Stoffe und Nähzubehör sucht Flyer-Design
Zielgruppe
Wir haben ein Fachgeschäft für Stoffe und Nähzubehör. Bei uns kaufen vorwiegend Frauen, vorwiegend Mütter und Großmütter, ein.
Aufgabenstellung
Hinweis auf verschiedene Stoffe (Jersey, Sweat, Baumwolle, Fleece, Softshell usw.) und breites Sortiment an Kurzwaren und Nähzubehör (Nähgarn, Reißverschlüsse, Bänder, Kordeln, usw.)
Evtl. sollte eine kleine Straßenkarte integriert werden.
Öffnungszeiten: Montag - Freitag 09:00-12:30 und 15:00-18:00, Mittwoch nachmittags geschlossen, Samstag 09:00-12:30

```html
<!DOCTYPE html>
<html lang="de">
<head>
<meta charset="utf-8">
<title>Nahtwerk – Flyer</title>
<link rel="stylesheet" href="https://fonts.googleapis.com/css2?family=Josefin+Sans:wght@300;400;600&family=Kaushan+Script&display=swap">
<style>
  :root {
    --stage: #4a4a4a;
    --paper: #ffffff;
    --teal: #8eacb4;
    --ink: #3d3d3d;
    --ink-soft: #555555;
    --cap: #ffffff;
    --shadow: rgba(0,0,0,0.45);
  }
  * { box-sizing: border-box; margin: 0; padding: 0; }
  html, body { width: 1197px; height: 1200px; overflow: hidden; background: var(--stage); }
  body { position: relative; font-family: "Josefin Sans", sans-serif; color: var(--ink); }

  .flyer {
    position: absolute; left: 75px; width: 1026px; height: 508px;
    background: var(--paper); box-shadow: 4px 5px 6px var(--shadow); overflow: hidden;
  }
  .flyer--front { top: 36px; }
  .flyer--back { top: 619px; }

  .photo { position: absolute; }

  /* Front */
  .brand-panel { position: absolute; left: 0; top: 0; width: 341px; height: 508px; }
  .brand-name {
    position: absolute; left: 0; width: 341px; top: 228px; text-align: center;
    font-weight: 600; font-size: 30px; letter-spacing: 3px; text-transform: uppercase; color: var(--ink);
  }
  .brand-mark {
    display: inline-block; width: 12px; height: 12px; border-radius: 50%;
    background: #d9553f; margin-left: 8px; vertical-align: 4px;
  }
  .tagline {
    position: absolute; left: 0; width: 341px; top: 455px; text-align: center;
    font-weight: 300; font-size: 14.5px; color: var(--ink-soft);
  }
  .photo--zipper { left: 341px; top: 0; width: 340px; height: 251px; background: linear-gradient(135deg, #d9d0cb, #b9aca6 60%, #c9a26a); }
  .photo--fabrics { left: 681px; top: 0; width: 345px; height: 251px; background: linear-gradient(90deg, #d8d5d2, #e7b8ad 35%, #b9c4c8 65%, #2f6466 85%, #cfd8da); }
  .photo--sewing-box { left: 341px; top: 258px; width: 340px; height: 250px; background: radial-gradient(ellipse at 50% 50%, #b9d3d6, #e6e6ea 65%); }
  .photo--fabric-stack { left: 681px; top: 258px; width: 345px; height: 250px; background: linear-gradient(90deg, #a0707c, #c9765a 30%, #b04a6a 55%, #3f7fc7 75%, #2a5fae); }

  /* Back */
  .photo--notions { left: 0; top: 0; width: 345px; height: 508px; background: radial-gradient(ellipse at 55% 40%, #f0ece8, #ffffff 70%); }
  .back-brand {
    position: absolute; left: 186px; top: 418px;
    font-weight: 600; font-size: 13px; letter-spacing: 1.3px; text-transform: uppercase; color: var(--ink);
  }
  .info {
    position: absolute; left: 345px; width: 343px; background: var(--teal);
  }
  .info--range { top: 0; height: 254px; }
  .info--hours { top: 262px; height: 246px; }
  .drop-cap {
    position: absolute; font-family: "Kaushan Script", cursive; color: var(--cap); line-height: 1;
  }
  .info--range .drop-cap { left: 40px; top: 30px; font-size: 86px; }
  .info--hours .drop-cap { left: 44px; top: 22px; font-size: 92px; }
  .lead { position: absolute; font-size: 14.5px; color: var(--ink); }
  .info--range .lead { left: 102px; top: 40px; }
  .info--hours .lead { left: 113px; top: 64px; }
  .range-list { position: absolute; left: 102px; top: 82px; width: 230px; }
  .range-list dt { font-weight: 600; font-size: 14.5px; line-height: 18px; margin-top: 4px; }
  .range-list dd { font-weight: 300; font-size: 13px; line-height: 18px; color: var(--ink); }
  .hours { position: absolute; left: 0; width: 343px; top: 92px; text-align: center; font-weight: 300; font-size: 14.5px; line-height: 21px; }
  .hours p + p { margin-top: 9px; }
  .hours .times span + span { margin-left: 14px; }
  .photo--pins { left: 688px; top: 0; width: 338px; height: 254px; background: linear-gradient(150deg, #d98c86, #c86e6a 55%, #b7a8a0); }
  .photo--machine { left: 688px; top: 262px; width: 338px; height: 246px; background: linear-gradient(180deg, #d7dbdd, #c6ccd0 55%, #2a2522 80%, #5a3a26); }
</style>
</head>
<body>

<section class="flyer flyer--front" aria-label="Flyer Vorderseite">
  <div class="brand-panel">
    <div class="brand-name">Nahtwerk<span class="brand-mark"></span></div>
    <p class="tagline">Fachgeschäft für Stoffe und Nähzubehör</p>
  </div>
  <div class="photo photo--zipper" role="img" aria-label="Foto: goldener Reißverschluss auf hellem Stoff"></div>
  <div class="photo photo--fabrics" role="img" aria-label="Foto: gemusterte Stoffe mit Schere"></div>
  <div class="photo photo--sewing-box" role="img" aria-label="Foto: Nähkästchen mit Garnrollen und Maßband"></div>
  <div class="photo photo--fabric-stack" role="img" aria-label="Foto: Stapel farbiger Stoffe"></div>
</section>

<section class="flyer flyer--back" aria-label="Flyer Rückseite">
  <div class="photo photo--notions" role="img" aria-label="Foto: Maßband, Garnrolle und Schere"></div>
  <div class="back-brand">Nahtwerk</div>

  <div class="info info--range">
    <span class="drop-cap">G</span>
    <p class="lead">rosse Auswahl an</p>
    <dl class="range-list">
      <dt>Stoffen</dt>
      <dd>Jersey, Sweat, Baumwolle,<br>Fleece, Softshell,...</dd>
      <dt>Kurzwaren und Nähzubehör</dt>
      <dd>Nähgarn, Reißverschlüsse,<br>Bänder, Kordeln,...</dd>
    </dl>
  </div>

  <div class="info info--hours">
    <span class="drop-cap">U</span>
    <p class="lead">nsere Öffnungszeiten:</p>
    <div class="hours">
      <p>Montag - Freitag<br><span class="times"><span>09:00-12:30</span><span>15:00-18:00 Uhr</span></span></p>
      <p>Samstag<br>09:00-12:30 Uhr</p>
      <p>Mittwoch nachmittags geschlossen</p>
    </div>
  </div>

  <div class="photo photo--pins" role="img" aria-label="Foto: Stecknadeln, Sicherheitsnadeln und Fingerhut"></div>
  <div class="photo photo--machine" role="img" aria-label="Foto: alte Nähmaschine"></div>
</section>

</body>
</html>
```